International Clinical Software Company needs a new business card design

We are looking for a new business card design for our company that has recently expanded into the UK market, making us a multinational company.
After having rebranded our website and produced a new style guide, we are looking for a business card that is creative and attention grabbing, while being consistent with the style and colour scheme used on the new website, www.brookvale.example
We produce care management technology for the aged care market, but the main aspect we aim to communicate is the human element of our software, and the way it assists in providing better care for aged people, and stronger relationships between aged people and the staff that care for them.
Our current business card is a dark green with gold text, which makes the text quite difficult to read, not very aesthetically appealing and the colour scheme looks quite dated.
We would like something fresh and modern, that can still be colourful but doesn't use large blocks of dark colour, and uses the colours within our logo.
Something tying in with the leaves that are used in our logo could work quite nicely, along with the Autumn/Fall colours of soft greens, yellows and reds (also in our existing logo). However also happy to look at fresh, completely out of the box ideas we may not have yet considered.
Target Market(s)
The people that receive this business card work in the aged card or health industry and are either corporate/management level staff or clinical (Registered Nurses, care workers etc.)
Industry/Entity Type
Health Product
Contact Information for Business Card
Company Name - BrookvaleTech
Company locations: Lymford Quay, Westshire, Northmere
Staff Details:
Staff name: Dermot Quill
Staff job title: Executive Chairman
Staff email: d.quill@brookvale.example
Office phone number: 01632 960418
Font styles to use
Other font styles liked:
- Calibri
Requirements
Must have
- Must include the BrookvaleTech brand name in it's current font
- Must include logo (3 leaves in gold circle)
- Must include Business Card Details
Nice to have
- Elements of gold
- White space
- Something autumn themed but not too cliched
Should not have
- No blue - used by a major competitor and we would like to differentiate from them
- Large blocks of dark green colour (the green that appears in our leaves on the logo on our current business card is the background colour and it is far too dark)

```html
<!DOCTYPE html>
<html lang="en">
<head>
<meta charset="utf-8">
<title>BrookvaleTech Business Card</title>
<link href="https://fonts.googleapis.com/css2?family=Open+Sans:wght@400;600&display=swap" rel="stylesheet">
<style>
  :root {
    --page-bg: #e9e7e3;
    --card-bg: #ffffff;
    --gold: #b89a3e;
    --gold-soft: #c8b27a;
    --taupe: #b3a07a;
    --text-dark: #2f2f2f;
    --text-mid: #555555;
    --leaf-brown: #b7782c;
    --leaf-yellow: #f0c43a;
    --leaf-red: #e2401c;
    --leaf-orange: #f5921e;
    --leaf-green: #a8c48a;
  }
  * { margin: 0; padding: 0; box-sizing: border-box; }
  html, body {
    width: 1200px; height: 900px; overflow: hidden;
    background: var(--page-bg);
    font-family: "Open Sans", Calibri, sans-serif;
  }
  .card {
    position: absolute; left: 100px; top: 160px;
    width: 1000px; height: 580px;
    background: var(--card-bg);
    box-shadow: 0 10px 30px rgba(0,0,0,0.18);
    overflow: hidden;
  }
  .brand {
    position: absolute; right: 70px; top: 44px;
    display: flex; flex-direction: column; align-items: center; gap: 18px;
  }
  .brand-mark {
    width: 130px; height: 130px; border-radius: 50%;
    background: var(--taupe);
  }
  .brand-name {
    font-size: 34px; font-weight: 400; color: var(--gold-soft);
    letter-spacing: 1px;
  }
  .rule {
    position: absolute; left: 330px; right: 70px; top: 300px;
    height: 1px; background: var(--gold-soft);
  }
  .person { position: absolute; left: 70px; top: 250px; }
  .person-name { font-size: 34px; font-weight: 400; color: var(--gold); line-height: 1.1; }
  .person-title { font-size: 22px; color: var(--text-mid); margin-top: 2px; }
  .contact {
    position: absolute; right: 70px; top: 322px;
    list-style: none; text-align: right;
    font-size: 19px; color: var(--text-dark); line-height: 34px;
  }
  .contact li { display: flex; justify-content: flex-end; align-items: center; gap: 12px; }
  .contact .icon { width: 20px; height: 20px; flex: none; }
  .leaf-band {
    position: absolute; left: 0; right: 0; bottom: 0; height: 92px;
    background: linear-gradient(90deg,
      var(--leaf-brown) 0%, var(--leaf-yellow) 6%, var(--leaf-yellow) 22%,
      var(--leaf-red) 34%, var(--leaf-orange) 50%, var(--leaf-red) 60%,
      var(--leaf-orange) 74%, var(--leaf-yellow) 86%, var(--leaf-green) 94%, var(--leaf-green) 100%);
  }
</style>
</head>
<body>
  <div class="card">
    <div class="brand">
      <div class="brand-mark"></div>
      <div class="brand-name">BrookvaleTech</div>
    </div>

    <div class="person">
      <div class="person-name">Dermot Quill</div>
      <div class="person-title">Executive Chairman</div>
    </div>

    <div class="rule"></div>

    <ul class="contact">
      <li>01632 960418
        <svg class="icon" viewBox="0 0 20 20" aria-hidden="true"><rect width="20" height="20" rx="3" fill="#b89a3e"/><path d="M5 8c0-2 2-3 5-3s5 1 5 3l-2 1-1-2H8L7 9 5 8zm2 2h6l1 4H6l1-4z" fill="#fff"/></svg>
      </li>
      <li>d.quill@brookvale.example
        <svg class="icon" viewBox="0 0 20 20" aria-hidden="true"><rect width="20" height="20" rx="3" fill="#b89a3e"/><rect x="4" y="6" width="12" height="8" fill="#fff"/><path d="M4 6l6 5 6-5" stroke="#b89a3e" stroke-width="1.2" fill="none"/></svg>
      </li>
      <li>BrookvaleTech
        <svg class="icon" viewBox="0 0 20 20" aria-hidden="true"><path d="M10 3l8 7h-3v7H5v-7H2z" fill="#b89a3e"/><rect x="8.5" y="12" width="3" height="5" fill="#fff"/></svg>
      </li>
      <li>Lymford Quay, Westshire, Northmere</li>
    </ul>

    <div class="leaf-band" role="img" aria-label="Photo strip of autumn leaves in yellow, red, orange and soft green"></div>
  </div>
</body>
</html>
```